Stationery Design Project for import company - Kelvo Trading

We are a import company that sells branded products to large retailers in New Zealand.
We need a simple, professional looking Logo, Business Cards, Email Signature and Letterhead.
Design needs to have some colour in it but nothing too bright or youthful.
The brand is business to business.
The companies name is Kelvo Trading.
I have uploaded some examples of business cards that I like
Also need a powerpoint template
The range of products is diverse so the deign needs to be generic. Please note that the business does not sell to consumers only other businesses
Target Market(s)
Buyers at Retail Companies Head Offices (business to business)
Industry/Entity Type
Business
Look and feel
Each slider illustrates characteristics of the customer's brand and the style your logo design should communicate.

```html
<!DOCTYPE html>
<html lang="en">
<head>
<meta charset="utf-8">
<title>Kelvo Trading Letterhead</title>
<link rel="stylesheet" href="https://fonts.googleapis.com/css2?family=Jost:wght@400;500;700&family=Michroma&display=swap">
<style>
  :root {
    --brand-blue: #1c4189;
    --brand-black: #000000;
    --header-grey: #f1f2f6;
    --paper: #ffffff;
    --mark-faint: #f0f1f6;
    --rule: #b9bfcc;
  }
  html, body { margin: 0; padding: 0; overflow: hidden; }
  body { width: 927px; height: 1200px; background: var(--paper); }
  .letterhead {
    position: relative; width: 927px; height: 1200px; overflow: hidden;
    background: var(--paper); font-family: "Jost", sans-serif;
  }
  .band { position: absolute; left: 0; display: block; }
  .band--top { top: 0; }
  .band--bottom { bottom: 0; }
  .header {
    position: absolute; top: 56px; left: 0; width: 927px; height: 137px;
    background: var(--header-grey);
  }
  .wordmark {
    position: absolute; left: 62px; top: 24px; margin: 0;
    display: flex; align-items: center; gap: 14px;
    font-family: "Michroma", sans-serif; font-size: 27px; font-weight: 400;
    color: var(--brand-blue); letter-spacing: 1px; line-height: 1.35; white-space: nowrap;
  }
  .wordmark__dot {
    display: block; width: 16px; height: 16px; background: var(--brand-blue); flex: none;
  }
  .wordmark__lines { display: block; }
  .wordmark__line { display: block; }
  .signatory {
    position: absolute; left: 390px; top: 50px; width: 185px; text-align: right;
  }
  .signatory__name {
    display: block; font-size: 24px; font-weight: 700; color: var(--brand-blue);
    line-height: 1; letter-spacing: -0.3px; text-align: left; white-space: nowrap;
  }
  .signatory__position {
    display: block; font-size: 12px; font-weight: 700; color: var(--brand-black);
    letter-spacing: 0.3px; margin-top: 2px;
  }
  .divider {
    position: absolute; left: 589px; top: 57px; width: 1px; height: 55px; background: var(--rule);
  }
  .contact {
    position: absolute; left: 605px; top: 52px; margin: 0; padding: 0; list-style: none;
  }
  .contact__item {
    display: flex; align-items: center; height: 21px;
    font-size: 17px; font-weight: 500; color: var(--brand-black); letter-spacing: 0.2px;
    white-space: nowrap;
  }
  .contact__icon { width: 20px; height: 14px; margin-right: 10px; flex: none; }
  .mark-faint {
    position: absolute; left: 0; top: 470px; width: 927px; text-align: center;
    font-family: "Michroma", sans-serif; font-size: 92px; color: var(--mark-faint);
    line-height: 1.35; white-space: nowrap; letter-spacing: 2px;
  }
  .mark-faint__line { display: block; }
  .footer-web {
    position: absolute; right: 62px; bottom: 24px; margin: 0;
    font-size: 22px; font-weight: 500; color: var(--paper); letter-spacing: 0.8px;
  }
</style>
</head>
<body>
<main class="letterhead">
  <svg class="band band--top" width="927" height="56" viewBox="0 0 927 56" aria-hidden="true">
    <polygon points="0,0 500,0 458,56 0,56" fill="var(--brand-blue)"/>
    <polygon points="510,0 927,0 927,56 468,56" fill="var(--brand-black)"/>
  </svg>

  <header class="header">
    <h1 class="wordmark">
      <span class="wordmark__dot"></span>
      <span class="wordmark__lines">
        <span class="wordmark__line">KELVO</span>
        <span class="wordmark__line">TRADING</span>
      </span>
    </h1>

    <div class="signatory">
      <span class="signatory__name">YOUR NAME.....</span>
      <span class="signatory__position">POSITION</span>
    </div>

    <div class="divider"></div>

    <ul class="contact">
      <li class="contact__item">
        <svg class="contact__icon" viewBox="0 0 20 14" aria-hidden="true">
          <path d="M1 5 Q10 -1 19 5 L17 7 L14 5 L14 3 Q10 2 6 3 L6 5 L3 7 Z" fill="var(--brand-black)"/>
          <rect x="4" y="7" width="12" height="7" rx="1" fill="var(--brand-black)"/>
        </svg>
        00 0000 0000
      </li>
      <li class="contact__item">
        <svg class="contact__icon" viewBox="0 0 20 14" aria-hidden="true">
          <rect x="1" y="1" width="18" height="12" fill="var(--brand-black)"/>
          <path d="M1 1 L10 8 L19 1" stroke="var(--paper)" stroke-width="1.3" fill="none"/>
        </svg>
        EMAIL@KELVOTRADING.COM
      </li>
      <li class="contact__item">
        <svg class="contact__icon" viewBox="0 0 20 14" aria-hidden="true">
          <circle cx="10" cy="7" r="6" fill="none" stroke="var(--brand-black)" stroke-width="1.6"/>
          <ellipse cx="10" cy="7" rx="2.5" ry="6" fill="none" stroke="var(--brand-black)" stroke-width="1.2"/>
          <line x1="4" y1="7" x2="16" y2="7" stroke="var(--brand-black)" stroke-width="1.2"/>
        </svg>
        WWW.YOURWEBSITE.COM
      </li>
    </ul>
  </header>

  <div class="mark-faint" aria-hidden="true">
    <span class="mark-faint__line">KELVO</span>
    <span class="mark-faint__line">TRADING</span>
  </div>

  <svg class="band band--bottom" width="927" height="60" viewBox="0 0 927 60" aria-hidden="true">
    <polygon points="0,0 505,0 470,60 0,60" fill="var(--brand-blue)"/>
    <polygon points="518,0 927,0 927,60 483,60" fill="var(--brand-black)"/>
  </svg>
  <p class="footer-web">WWW.YOURWEBSITE.COM</p>
</main>
</body>
</html>
```